Meridian Callware business card design

I would like to see some designs for a business card for Meridian Callware. I would like the business card to be double sided. It will need to have a similar colour / look and feel to our website www.meridiancallware.com.au I have also attached our latest flyer. Final designs to be handed over in Photoshop format so that I can edit the business card when needed please.

Industry/Entity Type

Business

Contact Information for Business Card

Kelvin Ashworth
sales@meridiancallware.com.au
Business Development Manager
ph: (08) 6517 2984
www.meridiancallware.com.au

Font styles to use
Serif
Sans Serif

Requirements
Must have
• If you could please utilise our colour scheme as seen on our website and the attached flyer.
• I would also like the final design to be in a Photoshop format so that I can edit it when needed please.

```html
<!DOCTYPE html>
<html lang="en">
<head>
<meta charset="utf-8">
<title>Meridian Callware – Business Card</title>
<link href="https://fonts.googleapis.com/css2?family=Montserrat:wght@500&family=Open+Sans:wght@400;700&display=swap" rel="stylesheet">
<style>
  :root {
    --stage: #d9dadc;
    --card-dark: #353535;
    --card-light: #ffffff;
    --ink: #2b2b2b;
    --ink-soft: #555555;
    --brand-blue: #1b7bc4;
    --mist: #e6eef6;
    --on-dark: #ffffff;
  }
  * { box-sizing: border-box; margin: 0; padding: 0; }
  html, body { width: 1200px; height: 900px; overflow: hidden; }
  body {
    background: var(--stage);
    display: flex;
    flex-direction: column;
    align-items: center;
    justify-content: center;
    gap: 50px;
  }
  .card {
    position: relative;
    width: 630px;
    height: 360px;
    box-shadow: 0 8px 24px rgba(0,0,0,0.18);
    overflow: hidden;
  }
  .card--back { background: var(--card-dark); }
  .card--front { background: var(--card-light); }

  .wordmark {
    font-family: "Montserrat", sans-serif;
    font-weight: 500;
    letter-spacing: 0.5px;
    white-space: nowrap;
  }
  .card--back .wordmark {
    position: absolute;
    left: 0; right: 0;
    top: 140px;
    text-align: center;
    font-size: 48px;
    color: var(--on-dark);
  }
  .card--back .web {
    position: absolute;
    left: 0; right: 0;
    bottom: 30px;
    text-align: center;
    font-family: "Open Sans", sans-serif;
    font-size: 13px;
    color: var(--on-dark);
    letter-spacing: 0.3px;
  }

  .front-deco {
    position: absolute;
    right: 110px;
    top: 30px;
  }
  .identity {
    position: absolute;
    left: 34px;
    top: 110px;
    font-family: "Open Sans", sans-serif;
  }
  .identity .name {
    font-weight: 700;
    font-size: 26px;
    letter-spacing: 1px;
    color: var(--ink);
    line-height: 1.1;
  }
  .identity .name .first { color: var(--brand-blue); }
  .identity .role {
    font-size: 14px;
    color: var(--ink-soft);
    margin-top: 2px;
  }
  .contacts {
    list-style: none;
    margin-top: 10px;
    margin-left: 2px;
  }
  .contacts li {
    display: flex;
    align-items: center;
    gap: 8px;
    font-size: 14px;
    color: var(--ink);
    line-height: 1.35;
  }
  .contacts svg { flex: none; }
  .card--front .wordmark {
    position: absolute;
    right: 34px;
    bottom: 40px;
    font-size: 38px;
    color: var(--ink);
  }
</style>
</head>
<body>
  <section class="card card--back">
    <div class="wordmark">Meridian Callware</div>
    <div class="web">www.meridiancallware.com.au</div>
  </section>

  <section class="card card--front">
    <svg class="front-deco" width="150" height="150" viewBox="0 0 150 150" aria-hidden="true">
      <circle cx="75" cy="75" r="70" fill="var(--mist)"/>
    </svg>

    <div class="identity">
      <div class="name"><span class="first">Kelvin</span> Ashworth</div>
      <div class="role">Business Development Manager</div>
      <ul class="contacts">
        <li>
          <svg width="12" height="12" viewBox="0 0 24 24"><path fill="var(--brand-blue)" d="M6.6 10.8a15 15 0 0 0 6.6 6.6l2.2-2.2c.3-.3.7-.4 1-.2 1.1.4 2.3.6 3.6.6.6 0 1 .4 1 1V20c0 .6-.4 1-1 1A17 17 0 0 1 3 4c0-.6.4-1 1-1h3.5c.6 0 1 .4 1 1 0 1.3.2 2.5.6 3.6.1.3 0 .7-.2 1z"/></svg>
          (08) 6517 2984
        </li>
        <li>
          <svg width="12" height="12" viewBox="0 0 24 24"><rect x="2" y="5" width="20" height="14" rx="2" fill="var(--brand-blue)"/><path d="M3 6l9 7 9-7" stroke="#fff" stroke-width="2" fill="none"/></svg>
          sales@meridiancallware.com.au
        </li>
        <li>
          <svg width="12" height="12" viewBox="0 0 24 24"><circle cx="12" cy="12" r="10" fill="var(--brand-blue)"/><path d="M2 12h20M12 2c3 3 3 17 0 20M12 2c-3 3-3 17 0 20" stroke="#fff" stroke-width="1.5" fill="none"/></svg>
          www.meridiancallware.com.au
        </li>
      </ul>
    </div>

    <div class="wordmark">Meridian Callware</div>
  </section>
</body>
</html>
```